Geschäftspapiere für Hundebetreuung
Zielgruppe
Mein Unternehmen richtet sich an Hundehalter, die freudig mit ihrem Hund arbeiten oder trainieren wollen oder eine positiv arbeitende Hundebetreuung oder Gassi-Gänger suchen. Hierbei liegt der Fokus auf Emotionen des Hundes, Emotionen des Hundehalters, Körpersprache und kleinschrittiges Training. Gemeinsames freudiges Training schafft Vertrauen und Bindung und ermöglicht Hund und Halter Freiraum. Ziel des Angebotes ist es, dass Hundehalter Verständnis für die Emotionen und Interessen des Hundes zu entwickeln und das für sich zu nutzen lernen, dem Hund das geben, was er in der jeweiligen Situation braucht und das ganze auf wissenschaftlich fundierter Basis.
Aufgabenstellung
Das Logo muss enthalten sein, ansonsten sind der Kreativität keine Grenzen gesetzt :)
Es sollte nur von Rechnung, über Angebot für alles nutzbar sein.
Das Unternehmen ist ein Einzelunternehmen, sprich der Firmenname ist mein eigener Name 'Sabine Krollmann' und Pfotenfreunde nur Website und Marke.

```html
<!DOCTYPE html>
<html lang="de">
<head>
<meta charset="utf-8">
<title>Pfotenfreunde – Briefbogen</title>
<link href="https://fonts.googleapis.com/css2?family=Poppins:wght@400;500;600;700&display=swap" rel="stylesheet">
<style>
  :root {
    --backdrop: #dcdcdc;
    --paper: #ffffff;
    --slate: #43565c;
    --green: #8dc22b;
    --ink: #3d4b50;
    --mist: #c9cccb;
    --footer-text: #e4e9ea;
  }
  * { box-sizing: border-box; margin: 0; padding: 0; }
  html, body { width: 1200px; height: 898px; overflow: hidden; }
  body {
    background: var(--backdrop);
    font-family: "Poppins", sans-serif;
    color: var(--ink);
  }
  .letterhead {
    position: absolute;
    left: 282px; top: 0;
    width: 635px; height: 898px;
    background: var(--paper);
    overflow: hidden;
  }
  .site-url {
    position: absolute; left: 58px; top: 56px;
    font-size: 10px; font-weight: 600; color: var(--slate);
  }
  .brand-mark {
    position: absolute; left: 440px; top: 58px;
    display: flex; align-items: center; gap: 8px;
  }
  .brand-mark .dot {
    width: 14px; height: 14px; border-radius: 50%; background: var(--green);
  }
  .brand-mark .name {
    font-size: 20px; font-weight: 600; color: var(--slate);
  }
  .sender-line {
    position: absolute; left: 72px; top: 150px;
    font-size: 6px; color: var(--green);
  }
  .sender-line b { font-weight: 600; }
  .recipient {
    position: absolute; left: 72px; top: 166px;
    font-size: 9.5px; line-height: 13px;
  }
  .recipient .company { font-weight: 600; }
  .date {
    position: absolute; right: 78px; top: 236px;
    font-size: 8.5px;
  }
  .fold-mark {
    position: absolute; left: 0; width: 22px; height: 1px; background: var(--mist);
  }
  .fold-mark.upper { top: 300px; }
  .fold-mark.lower { top: 600px; }
  .letter-body {
    position: absolute; left: 72px; top: 330px; width: 470px;
    font-size: 8.8px; line-height: 12.6px;
  }
  .letter-body .subject {
    font-size: 11.5px; font-weight: 600; margin-bottom: 12px;
  }
  .letter-body p { margin-bottom: 12.6px; }
  .closing { margin-top: 24px; }
  .footer-art {
    position: absolute; left: 0; top: 0; width: 635px; height: 898px;
  }
  .footer-info {
    position: absolute; left: 0; bottom: 0; width: 635px; height: 90px;
    font-size: 6.8px; line-height: 9.5px; color: var(--footer-text);
  }
  .footer-info .col { position: absolute; }
  .footer-info .brand {
    left: 60px; top: 42px; font-size: 10px; font-weight: 600; color: var(--green);
  }
  .footer-info .address { left: 215px; top: 22px; }
  .footer-info .contact { left: 335px; top: 4px; }
  .footer-info .bank { left: 470px; top: -6px; }
  .footer-info b { font-weight: 600; color: #fff; }
  .footer-info .label { color: var(--green); font-weight: 600; }
  .contact .row { display: flex; align-items: center; gap: 5px; }
  .contact svg { width: 6px; height: 6px; fill: var(--green); }
  .bank .grid { display: grid; grid-template-columns: 28px auto; }
</style>
</head>
<body>
<main class="letterhead">
  <div class="site-url">www.pfotenfreunde.de</div>
  <div class="brand-mark"><span class="dot"></span><span class="name">Pfotenfreunde</span></div>

  <div class="sender-line"><b>Pfotenfreunde GmbH</b> &nbsp;|&nbsp; Musterstraße 1 &nbsp;|&nbsp; 12345 Musterstadt</div>
  <address class="recipient" style="font-style:normal">
    <div class="company">Musterfirma GmbH</div>
    <div>Max Mustermann</div>
    <div>Musterstraße 123</div>
    <div>12345 Musterstadt</div>
  </address>
  <div class="date">Musterstadt, 01.01.2022</div>

  <span class="fold-mark upper"></span>
  <span class="fold-mark lower"></span>

  <article class="letter-body">
    <h1 class="subject">Betreff: Endam, omni dolor sam asperro que eos es</h1>
    <p>Uptassi quo volupta dit aliberis dolutas pelestrum sendi remquam repellent as autemodis etu­rit faciae illorrorest, omnimilit, qui ut endiscillam quid que sandero eiunt eror rest quam, tem­porunt officip sandam imi, sit acepudandis cor si cus, cum adios nonsedipsa consequ aesedit rem. Minus, inis am nos nossus vendaer uptiis mi, quiae con possi natis etur, simagna tionsed ullo venditia id ut auda isqui occus.</p>
    <p>Porest ma dolupta et accusdamusam sunt omnimil laborestia con commolum fugiaerio et iunt labor sequi velite et desciis sero modis nullandes del molliquo iliquis et eaquaspere sitiis es ele­nis dolendant exceperes es elenis dolendant exceperes es everest ibeatentia voloris ad millate il inctur? eatentia voloris ad millate il inctur? Qui vent venti ilibus.</p>
    <p>Excessi vel maximpo rporepe poreperum qui omniste eatenda quo es et omniaepudam, qui debissinci ullabor eptatempor modiorrum quos sus dolum ad quos et quias alissi debis nullore strunt porerum, sit vole.</p>
    <div class="closing">Herzlichst,<br>Erika Mustermann</div>
  </article>

  <svg class="footer-art" viewBox="0 0 635 898" aria-hidden="false">
    <defs>
      <linearGradient id="sceneTone" x1="0" y1="0" x2="0" y2="1">
        <stop offset="0" stop-color="#d6d8d7"/>
        <stop offset="1" stop-color="#c6c9c8"/>
      </linearGradient>
    </defs>
    <path role="img" aria-label="Dekorative Landschaft mit Bergen, Tannen, Person und Hund"
          d="M210 760 Q300 640 420 690 Q500 690 560 740 L560 790 Q400 800 210 800 Z"
          fill="url(#sceneTone)"/>
    <path d="M0 810 Q40 800 140 812 Q110 822 0 826 Z" fill="var(--green)"/>
    <path d="M0 822 Q120 826 230 790 Q420 720 635 735 L635 898 L0 898 Z" fill="var(--slate)"/>
  </svg>

  <footer class="footer-info">
    <div class="col brand">Pfotenfreunde GmbH</div>
    <div class="col address">
      Musterstraße 1<br>12345 Musterstadt<br><b>Geschäftsführung:</b><br>Erika Mustermann
    </div>
    <div class="col contact">
      <div class="row"><svg viewBox="0 0 10 10"><path d="M2 0l2 2-1 2q1 2 3 3l2-1 2 2-2 2Q2 9 0 2z"/></svg>+49 (0)1234 – 123 456 78</div>
      <div class="row"><svg viewBox="0 0 10 10"><rect x="2" y="0" width="6" height="10" rx="1"/></svg>+49 (0)1234 – 123 456 78</div>
      <div class="row"><svg viewBox="0 0 10 10"><rect x="0" y="2" width="10" height="7"/></svg>kontakt@pfotenfreunde.de</div>
      <div class="row"><b>www.pfotenfreunde.de</b></div>
    </div>
    <div class="col bank">
      <div class="label">Bankverbindung</div>
      <b>Musterbank AG</b>
      <div class="grid"><b>IBAN:</b><span>DE12 1234 1234 1234 1234 00</span><b>BIC:</b><span>ABCDEFGHJK</span></div>
    </div>
  </footer>
</main>
</body>
</html>
```